Business card

We are looking for a creative person to deigns our company business card.

Target Market(s)

College age student

Industry/Entity Type

Accommodation

Contact Information for Business Card

We want a fun, clean and sophisticated design. It should look good, but more importantly the information should be legible.

Font styles to use
Serif
Sans Serif
Other font styles liked:
• Open Sans ,

Colors
33a6d7

Requirements
Must have
• Must have a young and memorable message. Be legible.
• Our logo on the back on a solid blue , please find color and logo attached
• LodgeBridgely.net on the back.
Nice to have
• I would like to have couple of different fonts on the LodgeBridgely.net on the back of the cards with a solid blue.

```html
<!DOCTYPE html>
<html lang="en">
<head>
<meta charset="UTF-8">
<title>LodgeBridgely Business Card</title>
<link href="https://fonts.googleapis.com/css2?family=Open+Sans:wght@400;600;700&display=swap" rel="stylesheet">
<style>
  :root {
    --backdrop: #151515;
    --card-blue: #02558a;
    --brand-blue: #0b4f86;
    --white: #ffffff;
  }
  html, body {
    margin: 0;
    padding: 0;
    width: 1200px;
    height: 900px;
    overflow: hidden;
    background: var(--backdrop);
    font-family: "Open Sans", sans-serif;
  }
  .stage {
    position: relative;
    width: 1200px;
    height: 900px;
  }
  .card {
    position: absolute;
    top: 300px;
    width: 442px;
    height: 273px;
    overflow: hidden;
  }
  .card-front {
    left: 152px;
    background: var(--card-blue);
  }
  .card-back {
    left: 622px;
    background: var(--card-blue);
  }
  .brand-panel {
    position: absolute;
    left: 0;
    top: 0;
    width: 214px;
    height: 273px;
    background: var(--white);
    display: flex;
    align-items: center;
    justify-content: center;
  }
  .brand-name {
    font-family: "Open Sans", sans-serif;
    font-weight: 700;
    letter-spacing: -0.3px;
    margin: 0;
  }
  .brand-panel .brand-name {
    color: var(--brand-blue);
    font-size: 22px;
  }
  .card-back {
    display: flex;
    align-items: center;
    justify-content: center;
  }
  .card-back .brand-name {
    color: var(--white);
    font-size: 30px;
  }
  .person {
    position: absolute;
    left: 237px;
    top: 68px;
    color: var(--white);
  }
  .person-name {
    margin: 0;
    font-size: 20px;
    font-weight: 600;
    line-height: 26px;
  }
  .person-title {
    margin: 0;
    font-size: 14px;
    line-height: 18px;
  }
  .contact-list {
    position: absolute;
    left: 238px;
    top: 159px;
    margin: 0;
    padding: 0;
    list-style: none;
    color: var(--white);
    font-size: 14px;
    line-height: 19px;
  }
  .contact-list li {
    display: flex;
    align-items: center;
    gap: 8px;
  }
  .contact-icon {
    width: 10px;
    height: 10px;
    flex: none;
  }
</style>
</head>
<body>
<main class="stage">
  <section class="card card-front">
    <div class="brand-panel">
      <p class="brand-name">LodgeBridgely</p>
    </div>
    <div class="person">
      <p class="person-name">Daniel Harper</p>
      <p class="person-title">Managing Director</p>
    </div>
    <ul class="contact-list">
      <li>
        <svg class="contact-icon" viewBox="0 0 10 10" aria-hidden="true"><rect x="2.5" y="0.5" width="5" height="9" rx="1" fill="none" stroke="#fff" stroke-width="1.2"/><circle cx="5" cy="7.8" r="0.6" fill="#fff"/></svg>
        123-456-7890
      </li>
      <li>
        <svg class="contact-icon" viewBox="0 0 10 10" aria-hidden="true"><path d="M0.5 3.5 Q5 0.5 9.5 3.5 L8.5 5 L6.5 4 L6.5 3 Q5 2.5 3.5 3 L3.5 4 L1.5 5 Z" fill="#fff"/><rect x="2" y="5.5" width="6" height="3.5" rx="0.6" fill="#fff"/></svg>
        123-456-7890
      </li>
      <li>
        <svg class="contact-icon" viewBox="0 0 10 10" aria-hidden="true"><rect x="0.5" y="2" width="9" height="6.5" fill="#fff"/><path d="M0.8 2.3 L5 5.8 L9.2 2.3" fill="none" stroke="#02558a" stroke-width="0.9"/></svg>
        info@youremail.com
      </li>
      <li>
        <svg class="contact-icon" viewBox="0 0 10 10" aria-hidden="true"><g fill="none" stroke="#fff" stroke-width="1.2"><rect x="0.8" y="4.6" width="5" height="3" rx="1.5" transform="rotate(-45 3.3 6.1)"/><rect x="4.2" y="1.4" width="5" height="3" rx="1.5" transform="rotate(-45 6.7 2.9)"/></g></svg>
        www.yourweb.com
      </li>
    </ul>
  </section>
  <section class="card card-back">
    <p class="brand-name">LodgeBridgely</p>
  </section>
</main>
</body>
</html>
```